carpet cleaning flyer/leaflet modern/upmarket twist

We are Velvet Nest, We do carpet & upholstery cleaning for the domestic market, if you are able to incorporate images like the ones I have provided that would be awesome, please feel free to find similar! mine are only examples. id like a front cover photo with the company name running through it, and the back to be half picture and then the detailing of what we do which is in the document I've uploaded
Target Market(s)
Domestic house hold
Industry/Entity Type
Cleaning Service
Colors
eea4c8
e667a6
c3c3c3
cbcbcb
aaaaaa
f59296
Requirements
Must have
- It must be 2 sided also have A modern but upmarket feel, a luxury. a front picture with name on it, back page with picture and writing from the word document.
Nice to have
- a input from yourselves, your twist on it

```html
<!DOCTYPE html>
<html lang="en">
<head>
<meta charset="utf-8">
<title>Velvet Nest – Carpet &amp; Upholstery Cleaning Flyer</title>
<link rel="stylesheet" href="https://fonts.googleapis.com/css2?family=Montserrat:wght@600;700&family=Open+Sans:wght@400;700&display=swap">
<style>
  :root {
    --pink: #e667a6;
    --pink-soft: #eea4c8;
    --grey-light: #cbcbcb;
    --grey-mid: #aaaaaa;
    --grey-text: #555555;
    --charcoal: #3e3e40;
    --canvas-bg: #ececec;
    --white: #ffffff;
    --carpet-blue: #7d879d;
    --carpet-deep: #68728a;
    --carpet-clean: #b4bac6;
  }
  * { box-sizing: border-box; margin: 0; padding: 0; }
  html, body { width: 1200px; height: 1000px; overflow: hidden; }
  body { background: var(--canvas-bg); position: relative; font-family: "Open Sans", Arial, sans-serif; }

  .page {
    position: absolute; top: 142px; width: 527px; height: 745px; overflow: hidden;
    box-shadow: 0 6px 18px rgba(0,0,0,.25);
  }
  .page--front { left: 57px; }
  .page--back { left: 632px; background: linear-gradient(180deg, #ffffff 40%, #ececec 85%); }

  /* Front cover photo area */
  .cover-photo {
    position: absolute; inset: 0;
    background:
      radial-gradient(ellipse 150px 260px at 50% 92%, rgba(30,30,34,.55) 0%, rgba(30,30,34,.25) 45%, rgba(30,30,34,0) 100%),
      linear-gradient(90deg,
        rgba(255,255,255,0) 23%, rgba(255,255,255,.32) 26%,
        rgba(255,255,255,.36) 48%, rgba(255,255,255,.32) 69%,
        rgba(255,255,255,0) 72%),
      linear-gradient(165deg, #939cb0 0%, var(--carpet-blue) 45%, var(--carpet-deep) 100%);
  }
  .cover-brand { position: absolute; left: 146px; top: 150px; width: 216px; text-align: center; }
  .cover-brand__name {
    font-family: "Montserrat", Arial, sans-serif; font-weight: 700; color: var(--pink);
    font-size: 38px; line-height: 42px; letter-spacing: .5px;
  }
  .cover-brand__rule { height: 2px; background: var(--grey-mid); margin: 4px 0 6px; }
  .cover-brand__tag { font-size: 11.5px; color: #4a4a4a; letter-spacing: .3px; white-space: nowrap; }

  /* Back page */
  .back-photo {
    position: absolute; left: 0; top: 0; width: 527px; height: 315px;
    background: linear-gradient(160deg, #d8dbdc 0%, #a9abae 40%, #7b7d80 75%, #66686b 100%);
  }
  .back-shapes { position: absolute; left: 0; top: 0; }

  .feature { position: absolute; left: 0; width: 100%; }
  .feature--reliable { top: 340px; }
  .feature--professional { top: 442px; }
  .feature--trustworthy { top: 530px; }
  .feature__label { display: block; width: 205px; height: 28px; }
  .feature__text {
    margin: 10px 0 0 30px; white-space: nowrap;
    font-size: 12px; line-height: 16px; color: var(--grey-text);
  }
  .feature__text strong { color: #333; }

  .footer-brand { position: absolute; left: 30px; top: 676px; width: 212px; }
  .footer-brand__name {
    font-family: "Montserrat", Arial, sans-serif; font-weight: 700; color: #eeeeee;
    font-size: 22px; letter-spacing: .3px; white-space: nowrap;
  }
  .footer-brand__rule { height: 1px; background: var(--grey-mid); margin: 2px 0 4px; }
  .footer-brand__tag { font-size: 10.5px; color: var(--grey-light); text-align: center; white-space: nowrap; }

  .contact { position: absolute; left: 277px; top: 678px; }
  .contact__row { display: flex; align-items: center; gap: 8px; color: var(--pink); font-weight: 700; white-space: nowrap; }
  .contact__row--email { font-size: 13.5px; height: 22px; }
  .contact__row--phone { font-size: 19px; height: 28px; margin-top: 2px; }
</style>
</head>
<body>

<section class="page page--front">
  <div class="cover-photo" role="img" aria-label="Photo: a vacuum cleaner head pulling a freshly cleaned, lighter stripe up through a blue-grey carpet"></div>
  <div class="cover-brand">
    <h1 class="cover-brand__name">VELVET<br>NEST</h1>
    <div class="cover-brand__rule"></div>
    <p class="cover-brand__tag">CARPET &amp; UPHOLSTERY CLEANING</p>
  </div>
</section>

<section class="page page--back">
  <div class="back-photo" role="img" aria-label="Photo: bright living room with grey carpet, grey armchair with cushion, wire chair and round pouf by glass doors"></div>
  <svg class="back-shapes" width="527" height="745" viewBox="0 0 527 745" aria-hidden="true">
    <path d="M0 300 Q260 330 527 262 L527 320 L0 320 Z" fill="#ffffff"/>
    <path d="M0 300 Q260 330 527 262 L527 276 Q280 330 0 316 Z" fill="#e667a6"/>
    <path d="M0 665 Q250 590 527 668 L527 745 L0 745 Z" fill="#3e3e40"/>
    <path d="M0 660 Q250 585 527 662 L527 670 Q250 596 0 670 Z" fill="#e667a6"/>
  </svg>

  <div class="feature feature--reliable">
    <svg class="feature__label" viewBox="0 0 205 28" aria-hidden="true">
      <path d="M0 0 H205 L192 14 L205 28 H0 Z" fill="#e667a6"/>
      <text x="30" y="20" fill="#fff" font-family="Montserrat, Arial, sans-serif" font-weight="700" font-size="16">RELIABLE</text>
    </svg>
    <p class="feature__text">We pride ourselves on providing outstanding services to our customers.<br>From a single carpet or rug, to a whole-house clean, we provide a reliable<br>and friendly service. <strong>Call us to discuss your needs.</strong></p>
  </div>

  <div class="feature feature--professional">
    <svg class="feature__label" viewBox="0 0 205 28" aria-hidden="true">
      <path d="M0 0 H205 L192 14 L205 28 H0 Z" fill="#e667a6"/>
      <text x="30" y="20" fill="#fff" font-family="Montserrat, Arial, sans-serif" font-weight="700" font-size="16">PROFESSIONAL</text>
    </svg>
    <p class="feature__text">We use the latest hot water extraction cleaning technology to give us<br>the ability to get into the ground down dirt deep down inside the Fibres.</p>
  </div>

  <div class="feature feature--trustworthy">
    <svg class="feature__label" viewBox="0 0 205 28" aria-hidden="true">
      <path d="M0 0 H205 L192 14 L205 28 H0 Z" fill="#e667a6"/>
      <text x="30" y="20" fill="#fff" font-family="Montserrat, Arial, sans-serif" font-weight="700" font-size="16">TRUSTWORTHY</text>
    </svg>
    <p class="feature__text">We are fully insured to work in your home, we guarantee all our work so<br>if any issues do arise we will do our up most to put it back right for you.</p>
  </div>

  <div class="footer-brand">
    <p class="footer-brand__name">VELVET NEST</p>
    <div class="footer-brand__rule"></div>
    <p class="footer-brand__tag">CARPET &amp; UPHOLSTERY CLEANING</p>
  </div>

  <div class="contact">
    <p class="contact__row contact__row--email">
      <svg width="20" height="14" viewBox="0 0 20 14" aria-hidden="true"><rect x="1" y="1" width="18" height="12" fill="none" stroke="#aaaaaa" stroke-width="1.6"/><path d="M1 1 L10 8 L19 1" fill="none" stroke="#aaaaaa" stroke-width="1.6"/></svg>
      sam.hale@velvetnest.co.uk
    </p>
    <p class="contact__row contact__row--phone">
      <svg width="20" height="20" viewBox="0 0 20 20" aria-hidden="true"><circle cx="10" cy="10" r="8.8" fill="none" stroke="#aaaaaa" stroke-width="1.5"/><path d="M7 5.5 L8.6 5.5 L9.2 8 L8.1 8.9 Q9 11 11.1 11.9 L12 10.8 L14.5 11.4 L14.5 13 Q10 13.6 7.8 11 Q6 9 7 5.5 Z" fill="#aaaaaa"/></svg>
      01632 960 418
    </p>
  </div>
</section>

</body>
</html>
```